Design a corporate looking website for Harbourline Funding

Need design only WordPress mock up for Harbourline Funding who provides short term finance solutions to other businesses. We need a corporate looking website that depicts a trustworthy, Dynamic fast acting company.
Visit http://q7.pagemockery.net/ for current mock up We need something like e this but not the same with a design that depicts corporate with more colour and images, needs to install trust and fast action. Please feel free to change the layout as I am not wedded to current design but am happy with what on the landing page.

Target Market(s)

Small to medium sized Businesses

Industry/Entity Type

Finance

Number of Pages Required

1 page

Font styles to use
Sans Serif

Requirements
Must have
• Design Landing pages in WordPress
• Visit http://q7.pagemockery.net/ for current mock up need Layout like this but with a design that depicts corporate with more colour and images, needs to install trust and fast action. Please feel free to change the layout as I am not happy with current design but am wedded to what on the landing page.
Should not have
• any copyright material on it.

```html
<!DOCTYPE html>
<html lang="en">
<head>
<meta charset="utf-8">
<title>Harbourline Funding</title>
<link href="https://fonts.googleapis.com/css2?family=Exo+2:ital,wght@0,400;0,500;0,600;1,400;1,500&family=Open+Sans:wght@400;600&display=swap" rel="stylesheet">
<style>
  :root {
    --navy: #0e2a5c;
    --blue: #1c6fb0;
    --sky: #4aa8dc;
    --hero-top: #62bde8;
    --hero-bottom: #8fd2f2;
    --button: #1780b3;
    --heading: #3e77b0;
    --muted: #9aa6b4;
    --body: #3a3a46;
    --lavender: #a9a6ee;
    --footer-top: #aebde8;
    --footer-bottom: #1e3f8a;
    --white: #ffffff;
  }
  * { margin: 0; padding: 0; box-sizing: border-box; }
  html, body { width: 720px; height: 1200px; overflow: hidden; background: var(--white); }
  body { position: relative; font-family: "Open Sans", Arial, sans-serif; color: var(--body); }

  .site-header { position: absolute; top: 0; left: 0; width: 720px; height: 77px; display: flex; align-items: center; padding: 0 73px; }
  .brand { display: flex; align-items: center; gap: 7px; font-family: "Exo 2", sans-serif; font-weight: 600; font-size: 14px; color: var(--navy); white-space: nowrap; }
  .brand-dot { width: 18px; height: 18px; border-radius: 50%; background: var(--blue); flex: none; }
  .main-nav { margin-left: auto; display: flex; gap: 10px; font-family: "Exo 2", sans-serif; font-size: 10px; white-space: nowrap; }
  .main-nav a { color: var(--navy); text-decoration: none; }
  .header-band { position: absolute; top: 77px; left: 0; width: 720px; height: 9px; background: var(--sky); }

  .hero { position: absolute; top: 86px; left: 0; width: 720px; height: 330px; background: linear-gradient(160deg, var(--hero-top), var(--hero-bottom) 55%, var(--hero-top)); text-align: center; }
  .hero-mark { position: absolute; left: 310px; top: 42px; width: 100px; height: 100px; border-radius: 50%; background: var(--blue); opacity: .85; }
  .hero-brand { position: absolute; top: 152px; width: 100%; font-family: "Exo 2", sans-serif; font-weight: 600; font-size: 17px; color: var(--navy); }
  .hero-title { position: absolute; top: 200px; width: 100%; font-family: "Exo 2", sans-serif; font-weight: 500; font-size: 24px; color: #0c1830; }
  .hero-tagline { position: absolute; top: 228px; width: 100%; font-family: "Exo 2", sans-serif; font-weight: 500; font-size: 13px; color: #0c1830; }
  .hero-button { position: absolute; top: 252px; left: 306px; width: 115px; height: 37px; line-height: 37px; background: var(--button); color: var(--white); font-family: "Exo 2", sans-serif; font-size: 14px; border-radius: 2px; text-decoration: none; }

  .services-title { position: absolute; top: 440px; width: 100%; text-align: center; font-family: "Exo 2", sans-serif; font-weight: 500; font-size: 21px; color: var(--heading); }
  .services-rule { position: absolute; top: 477px; left: 73px; width: 574px; height: 1px; background: #eef0f4; }
  .service { position: absolute; display: flex; align-items: center; gap: 10px; font-family: "Exo 2", sans-serif; font-size: 11.5px; color: var(--muted); text-decoration: underline; white-space: nowrap; }
  .service-dot { width: 32px; height: 32px; border-radius: 50%; background: var(--blue); flex: none; }

  .why { position: absolute; top: 701px; left: 0; width: 720px; height: 176px; background: linear-gradient(180deg, #f4f5fb 0%, #dcdcf6 55%, var(--lavender) 100%); }
  .why-title { margin-top: 10px; text-align: center; font-family: "Exo 2", sans-serif; font-weight: 500; font-size: 20px; color: #7d9bc4; }
  .why-text { margin: 12px 73px 0; font-size: 9.6px; line-height: 15px; color: var(--body); text-align: justify; }

  .testimonial-photo { position: absolute; top: 915px; left: 129px; width: 76px; height: 76px; border-radius: 50%; background: radial-gradient(circle at 50% 40%, #d9b8a0, #3a2a26 75%); }
  .testimonial-quote { position: absolute; top: 934px; left: 224px; width: 420px; font-family: "Exo 2", sans-serif; font-style: italic; font-size: 12px; line-height: 16px; color: #b3bac4; }
  .testimonial-name { position: absolute; top: 996px; left: 100px; width: 136px; text-align: center; font-family: "Exo 2", sans-serif; font-style: italic; font-weight: 500; font-size: 12px; color: #6a7280; }

  .site-footer { position: absolute; top: 1044px; left: 0; width: 720px; height: 156px; background: linear-gradient(180deg, var(--footer-top), #6f8cd0 50%, var(--footer-bottom)); }
  .footer-nav { position: absolute; top: 44px; width: 100%; display: flex; justify-content: center; gap: 25px; font-family: "Exo 2", sans-serif; font-size: 12px; letter-spacing: 1.2px; white-space: nowrap; }
  .footer-nav a { color: var(--white); text-decoration: none; }
  .copyright { position: absolute; bottom: 10px; width: 100%; text-align: center; font-family: "Exo 2", sans-serif; font-style: italic; font-size: 9.5px; color: var(--white); }
</style>
</head>
<body>
  <header class="site-header">
    <div class="brand"><span class="brand-dot"></span>Harbourline Funding</div>
    <nav class="main-nav">
      <a href="#">Home</a><a href="#">Service</a><a href="#">Why Commission</a><a href="#">Investor</a><a href="#">About Us</a><a href="#">Contact Us</a><a href="#">Members Login</a>
    </nav>
  </header>
  <div class="header-band"></div>

  <section class="hero" role="img" aria-label="Photo of glass office towers seen from below, tinted sky blue">
    <div class="hero-mark"></div>
    <p class="hero-brand">Harbourline Funding</p>
    <h1 class="hero-title">Commission Assistant</h1>
    <p class="hero-tagline">Providing Commission Advance When you need it</p>
    <a class="hero-button" href="#">Get Started</a>
  </section>

  <h2 class="services-title">Our Services</h2>
  <div class="services-rule"></div>
  <a class="service" style="top:495px;left:73px"><span class="service-dot"></span>Residential Real Estate Agent</a>
  <a class="service" style="top:548px;left:73px"><span class="service-dot"></span>Commercial Real Estate Agent</a>
  <a class="service" style="top:599px;left:73px"><span class="service-dot"></span>Office Equipment &amp; Technology Agent</a>
  <a class="service" style="top:649px;left:73px"><span class="service-dot"></span>Mortgage &amp; Finance Brokers</a>
  <a class="service" style="top:495px;left:389px"><span class="service-dot"></span>Financial Planner</a>
  <a class="service" style="top:548px;left:389px"><span class="service-dot"></span>Medical &amp; Dental Equipment</a>
  <a class="service" style="top:599px;left:389px"><span class="service-dot"></span>Motor Vehicle &amp; Earth Moving Equipment</a>
  <a class="service" style="top:649px;left:389px"><span class="service-dot"></span>Telecommunications</a>

  <section class="why" role="img" aria-label="Faint photo of office buildings under a lavender wash">
    <h2 class="why-title">Why Harbourline Funding</h2>
    <p class="why-text">At Harbourline Funding our aim is to provide immediate commission advance solutions for all industries. Our background is sales, property and finance and we understand the issues faced with Small to medium Businesses, Agents, contractors and consultants who earn commissions. Unforeseen expenses, inconsistent sales, holiday periods, sickness, taxation bills and job changes can all have an effect on a sales and commission flow. Harbourline Funding are here to help if you have outstanding commissions that could be used now then we may have an answer, once approved you will have an advance on your outstanding commission within 4 hours.</p>
  </section>

  <div class="testimonial-photo" role="img" aria-label="Portrait photo of the client giving the testimonial"></div>
  <p class="testimonial-quote">“Great services. Very professional. Of course, this is just a placeholder testimonial, it will have to be replaced.”</p>
  <p class="testimonial-name">Marisa Delgado</p>

  <footer class="site-footer" role="img" aria-label="Photo of a bright modern office interior in blue tones">
    <nav class="footer-nav">
      <a href="#">Home</a><a href="#">Service</a><a href="#">Why Commission</a><a href="#">Investor</a><a href="#">About Us</a><a href="#">Contact Us</a>
    </nav>
    <p class="copyright">Copyright © 2016: Harbourline Funding. All rights reserved.</p>
  </footer>
</body>
</html>
```